Berrocal Tizón Law Firm for Small and Medium Business: Website

We need a web design that includes coding for the Wix platform, for a new company based in Santiago, Chile, called Berrocal Tizón, Abogados y Consultores. The company is essentially a law firm, with additional advisory services in accounting, tax management and finance. The main target of the company are founders, CEOs or C-level executives of small or medium companies based in Chile.
The main menu of the web page must have the following tab options:
- Home - About us - Services – How we work -Blog – FAQ -Contact
Our main services are:

1.- Commercial and corporate law advisory
2.- Legal defense in civil, criminal, labor and family matters (litigation and arbitration)
3.- Bankruptcy and reorganization of companies
4.- Collection and recovery of assets
5.- Asset protection
6.- Financial and tax advice

We want to highlight the following services:

-Bankruptcy and reorganization of companies
-Judicial defense in civil matters
-Financial and tax advice

In addition to these services, the following will be offered:
-Lawyer at your home for special cases
-Half hour free consultation
-Monthly service packages

The final design should communicate confidence, business savvy and high execution standards and quality.

Target Market(s)

The main target of the company are founders, CEOs or C-level executives of small or medium companies based in Chile.

Industry/Entity Type

Legal industry

Coding

Number of Pages Required

5+ page

Font styles to use
Serif

Requirements
Must have
• 1. Big banners para destacar los siguientes servicios: -Bankruptcy and reorganization of companies -Judicial defense in civil matters -Financial and tax advice 2. Call to action para agendar consulta legal. 3. Destacar los siguientes servicios: -Lawyer at your home for special cases -Half hour free consultation -Monthly service packages 3. Página para explicar cómo se cobra (precios transparentes): ver el siguiente sitio web: https://www.brookvanelegal.example/how 4. Links to Facebook, Instagram and Linkedin 5. Connection to Whatsapp.
Should not have
• Look old fashioned

```html
<!DOCTYPE html>
<html lang="en">
<head>
<meta charset="utf-8">
<title>Berrocal Tizón, Abogados y Consultores</title>
<link href="https://fonts.googleapis.com/css2?family=Tinos:ital,wght@0,400;0,700;1,400&family=Arimo:ital,wght@0,400;0,700;1,400&family=Poppins:wght@400;500;600&display=swap" rel="stylesheet">
<style>
:root{
  --green:#1b3329;
  --green-deep:#13261e;
  --gold:#c7a637;
  --gold-light:#e6d173;
  --gold-dark:#9e8222;
  --ink:#2a2a2a;
  --muted:#6b6b6b;
  --white:#ffffff;
  --serif:"Tinos",serif;
  --sans:"Arimo",sans-serif;
  --ui:"Poppins",sans-serif;
}
*{margin:0;padding:0;box-sizing:border-box}
html,body{width:1200px;height:4286px;overflow:hidden;background:var(--white)}
body{position:relative;font-family:var(--sans);color:var(--ink)}
.abs{position:absolute}
.photo{position:absolute}
.btn-gold{position:absolute;display:flex;align-items:center;justify-content:center;background:linear-gradient(180deg,var(--gold-light),var(--gold) 55%,var(--gold-dark));color:#1d1d1d;font-family:var(--sans);font-weight:700;text-transform:uppercase;letter-spacing:.3px;box-shadow:0 3px 6px rgba(0,0,0,.25)}

/* hero */
.hero{position:absolute;left:0;top:0;width:1200px;height:667px;background:linear-gradient(100deg,#b9b6ae 0%,#8c8a82 35%,#6b4a35 60%,#3e2c22 100%)}
.hero-nav{position:absolute;left:0;top:0;width:1200px;height:103px;background:rgba(60,66,62,.55)}
.brand{position:absolute;left:111px;top:28px;display:flex;align-items:center;gap:12px;font-family:var(--serif);font-size:34px;color:var(--gold-light)}
.brand-mark{width:44px;height:44px;background:var(--gold)}
.menu{position:absolute;top:38px;left:506px;display:flex;gap:28px;font-family:var(--serif);font-size:13.5px;color:var(--white);text-transform:uppercase}
.menu .active{border-bottom:2px solid var(--gold);padding-bottom:6px}
.hero-band{position:absolute;left:0;top:233px;width:1200px;height:241px;background:linear-gradient(90deg,rgba(70,74,70,.55),rgba(70,74,70,.25) 55%,rgba(0,0,0,0))}
.hero-title{position:absolute;left:111px;top:252px;font-family:var(--serif);font-size:62px;color:var(--white);letter-spacing:1px}
.hero-sub{position:absolute;left:111px;top:330px;font-family:var(--sans);font-weight:700;font-size:22px;color:var(--white)}
.socials{position:absolute;display:flex;gap:9px}
.socials span{width:30px;height:30px;border:1.5px solid currentColor;border-radius:50%}
.slide-arrow{position:absolute;width:43px;height:43px;display:flex;align-items:center;justify-content:center}

/* about */
.about-block{left:343px;top:750px;width:256px;height:457px;background:var(--green)}
.eyebrow{font-family:var(--sans);font-size:17px;letter-spacing:5px;color:var(--gold);text-transform:uppercase}
.h-serif{font-family:var(--serif);color:#1b1b1b;text-transform:uppercase}
.about-text{left:624px;top:853px;width:462px;font-size:13.3px;line-height:22.2px;color:#555;text-align:justify}

/* highlight */
.highlight{left:0;top:1290px;width:1200px;height:677px;background:radial-gradient(ellipse at 50% 30%,#22402f,var(--green-deep) 75%)}
.hl-card{position:absolute;top:1463px;width:313px;height:369px;border:2px solid var(--gold);background:linear-gradient(180deg,#8f8a83,#4a4640 70%,#2c2a26)}
.hl-card p{position:absolute;left:0;right:0;bottom:40px;text-align:center;font-family:var(--serif);font-size:17px;line-height:26px;color:var(--white)}
.diamond{position:absolute;top:1811px;width:42px;height:42px;transform:rotate(45deg);background:linear-gradient(135deg,var(--gold-light),var(--gold-dark))}
.chev{position:absolute;top:1822px;width:20px;height:20px}

/* services */
.svc{position:absolute;top:2133px;width:313px}
.svc .img{height:210px}
.svc h3{margin-top:21px;font-family:var(--serif);font-weight:400;font-size:20px;line-height:26px;letter-spacing:.6px;color:#333;text-transform:uppercase}
.svc p{margin-top:12px;font-size:12.5px;line-height:21px;color:#666}
.svc a{display:inline-block;margin-top:12px;font-size:13.5px;font-weight:700;color:#222;text-decoration:underline;text-underline-offset:3px}

/* testimonial */
.testi{left:0;top:2608px;width:1200px;height:434px}
.testi-quote{left:111px;top:2740px;width:370px;font-style:italic;font-size:13.5px;line-height:22.4px;color:#2a2a20}
.sq-btn{position:absolute;top:2910px;width:42px;height:42px;background:#111;display:flex;align-items:center;justify-content:center}

/* blog */
.card{position:absolute;background:var(--white);box-shadow:0 0 8px rgba(0,0,0,.14)}
.blog-title{font-family:var(--ui);font-weight:600;font-size:14px;line-height:23px;color:#1e1e1e;text-transform:uppercase}
.blog-ex{font-family:var(--ui);font-size:13px;line-height:25px;color:#666}

/* footer */
.footer{left:0;top:3816px;width:1200px;height:470px;background:var(--green)}
.f-head{position:absolute;top:3918px;font-family:var(--ui);font-weight:600;font-size:14.5px;color:var(--white);text-transform:uppercase}
.f-list{position:absolute;top:3952px;list-style:none;font-family:var(--ui);font-size:13.5px;line-height:28.3px;color:var(--white)}
.f-bottom{position:absolute;top:4196px;font-family:var(--ui);font-size:13.5px;color:var(--white)}
</style>
</head>
<body>

<!-- hero -->
<section class="hero" role="img" aria-label="Photo of two lawyers in business suits talking on a leather sofa in a bright office"></section>
<div class="hero-nav"></div>
<div class="brand"><span class="brand-mark"></span>Berrocal Tizón</div>
<nav class="menu">
  <span class="active">Home</span><span>About us</span><span>Services</span><span>How we work</span><span>Blog</span><span>FAQ</span><span>Contact</span>
</nav>
<div class="hero-band"></div>
<h1 class="hero-title" style="font-weight:400">BERROCAL TIZÓN</h1>
<p class="hero-sub">ABOGADOS Y CONSULTORES</p>
<a class="btn-gold" style="left:111px;top:379px;width:295px;height:42px;font-size:14px">Half hour free consultation</a>
<div class="socials" style="left:111px;top:587px;color:#222" aria-label="Facebook, Instagram and LinkedIn links"><span></span><span></span><span></span></div>
<div class="slide-arrow" style="left:996px;top:584px;background:#111"><svg width="14" height="14" viewBox="0 0 14 14"><path d="M9 2 4 7l5 5" stroke="#fff" stroke-width="2" fill="none"/></svg></div>
<div class="slide-arrow" style="left:1046px;top:584px;background:var(--gold)"><svg width="14" height="14" viewBox="0 0 14 14"><path d="m5 2 5 5-5 5" stroke="#fff" stroke-width="2" fill="none"/></svg></div>

<!-- about -->
<div class="abs about-block"></div>
<div class="photo" style="left:111px;top:770px;width:472px;height:417px;background:linear-gradient(135deg,#dfe3e4,#b9b4ab 50%,#6f6a64)" role="img" aria-label="Photo of three colleagues reviewing documents around a table"></div>
<p class="abs eyebrow" style="left:625px;top:768px">About us</p>
<h2 class="abs h-serif" style="left:624px;top:795px;font-size:42px;font-weight:400">Berrocal Tizón</h2>
<p class="abs about-text">Lorem ipsum dolor sit amet, consectetur adipiscing elit, sed do eiusmod tempor incididunt ut labore et dolore magna aliqua. Ut enim ad minim veniam, quis nostrud exercitation ullamco laboris nisi ut aliquip ex ea commodo consequat. Duis aute irure dolor in reprehenderit in voluptate velit esse cillum dolore eu fugiat nulla pariatur. Excepteur sint occaecat cupidatat non proident, sunt in culpa qui officia deserunt mollit anim id est laborum. Lorem ipsum dolor sit amet, consectetur adipiscing elit, sed do eiusmod tempor incididunt ut labore et dolore magna aliqua. Ut enim ad minim veniam, quis nostrud exercitation ullamco laboris nisi ut aliquip ex ea commodo consequat. Duis aute irure dolor in reprehenderit in voluptate velit esse cillum dolore eu fugiat nulla pariatur. Excepteur sint occaecat cupidatat non proident, sunt in culpa qui officia deserunt</p>
<a class="btn-gold" style="left:624px;top:1138px;width:379px;height:47px;font-size:14.5px">Lawyer at your home for special cases</a>

<!-- highlight services -->
<section class="abs highlight"></section>
<h2 class="abs h-serif" style="left:0;width:1200px;top:1383px;text-align:center;font-size:42px;font-weight:400;color:var(--white)">Highlight Services</h2>
<div class="hl-card" style="left:111px" role="img" aria-label="Photo of a thoughtful businessman at his laptop"><p>Bankruptcy and reorganization<br>of companies</p></div>
<div class="hl-card" style="left:443px" role="img" aria-label="Photo of a client reviewing papers with a lawyer"><p>Judicial defense in civil matters</p></div>
<div class="hl-card" style="left:774px" role="img" aria-label="Photo of two advisers meeting at a table"><p>Financial and tax advice</p></div>
<div class="diamond" style="left:247px"></div><svg class="chev" style="left:258px" viewBox="0 0 20 20"><path d="m7 3 7 7-7 7" stroke="#222" stroke-width="2" fill="none"/></svg>
<div class="diamond" style="left:579px"></div><svg class="chev" style="left:590px" viewBox="0 0 20 20"><path d="m7 3 7 7-7 7" stroke="#222" stroke-width="2" fill="none"/></svg>
<div class="diamond" style="left:910px"></div><svg class="chev" style="left:921px" viewBox="0 0 20 20"><path d="m7 3 7 7-7 7" stroke="#222" stroke-width="2" fill="none"/></svg>

<!-- services -->
<h2 class="abs h-serif" style="left:0;width:1200px;top:2062px;text-align:center;font-size:40px;font-weight:400;color:#222">Services</h2>
<article class="svc" style="left:111px">
  <div class="img" style="background:linear-gradient(135deg,#f1f2f2,#c9c6c0 60%,#4a5363)" role="img" aria-label="Photo of a lawyer meeting a couple at their home"></div>
  <h3>Lawyer at your home for<br>special cases</h3>
  <p>Sed ut perspiciatis unde omnis iste natus error sit voluptatem accusantium dolorem</p>
  <a>LEARN MORE →</a>
</article>
<article class="svc" style="left:443px">
  <div class="img" style="background:linear-gradient(135deg,#e8e6e2,#b8c3cc 50%,#c5733a)" role="img" aria-label="Photo of a tablet showing financial charts"></div>
  <h3>Half hour free<br>consultation</h3>
  <p>Sed ut perspiciatis unde omnis iste natus error sit voluptatem accusantium dolorem</p>
  <a>LEARN MORE →</a>
</article>
<article class="svc" style="left:774px">
  <div class="img" style="background:linear-gradient(135deg,#eceae6,#b7aa98 55%,#8a5a36)" role="img" aria-label="Photo of an adviser with a senior client at a laptop"></div>
  <h3>Monthly service packages</h3>
  <p style="margin-top:38px">Sed ut perspiciatis unde omnis iste natus error sit voluptatem accusantium dolorem</p>
  <a>LEARN MORE →</a>
</article>

<!-- testimonials -->
<div class="photo testi" style="background:linear-gradient(90deg,#d9d7d2,#bfc3c6 60%,#9aa2a8)" role="img" aria-label="Photo of two smiling business colleagues in blue suits"></div>
<svg class="abs" style="left:0;top:2608px" width="600" height="434" viewBox="0 0 600 434">
  <defs><linearGradient id="goldPanel" x1="0" y1="0" x2="1" y2="1"><stop offset="0" stop-color="#c8a93a"/><stop offset=".55" stop-color="#e3d07a"/><stop offset="1" stop-color="#b8982e"/></linearGradient></defs>
  <polygon points="0,0 483,0 591,434 0,434" fill="url(#goldPanel)"/>
</svg>
<h2 class="abs h-serif" style="left:111px;top:2674px;font-size:38px;font-weight:400;color:#222">Testimonials</h2>
<p class="abs testi-quote">"Lorem ipsum dolor sit amet, consectetur adipiscing elit, sed do eiusmod tempor incididunt ut labore et dolore magna aliqua. Ut enim ad minim veniam, quis nostrud exercitation ullamco laboris nisi ut aliquip ex ea commodo consequat. Duis aute irure dolor in reprehenderit"</p>
<p class="abs" style="left:114px;top:2863px;font-family:var(--serif);font-size:21px;color:#222">- Tomás Reyes</p>
<div class="sq-btn" style="left:116px"><svg width="12" height="12" viewBox="0 0 12 12"><path d="M8 1 3 6l5 5" stroke="#fff" stroke-width="2" fill="none"/></svg></div>
<div class="sq-btn" style="left:168px;background:var(--green)"><svg width="12" height="12" viewBox="0 0 12 12"><path d="m4 1 5 5-5 5" stroke="#fff" stroke-width="2" fill="none"/></svg></div>

<!-- latest blog -->
<h2 class="abs h-serif" style="left:0;width:1200px;top:3136px;text-align:center;font-size:38px;font-weight:400;color:#222">Latest Blog</h2>
<article class="card" style="left:111px;top:3198px;width:468px;height:513px">
  <div style="margin:5px 5px 0;height:250px;background:linear-gradient(180deg,#6f757b,#3d4247)" role="img" aria-label="Illustration of a money bag beside a rising red arrow"></div>
  <h3 class="blog-title" style="margin:34px 24px 0">Sed ut perspiciatis unde omnis iste natus error sit voluptatem accusantium</h3>
  <div style="display:flex;gap:46px;margin:16px 24px 0;font-family:var(--ui);font-size:11.5px;color:#777">
    <span><span style="color:var(--gold)">▣</span> 27/02/2020</span><span><span style="color:var(--gold)">●</span> Ana Ferrer</span><span><span style="color:var(--gold)">◆</span> 1,000</span>
  </div>
  <p class="blog-ex" style="margin:14px 24px 0">Natur aut odit aut fugit, sed quia consequuntur magni dolores eos qui ratione voluptatem sequi nesciunt.</p>
  <a class="btn-gold" style="left:24px;top:448px;width:156px;height:46px;font-family:var(--ui);font-weight:600;font-size:12.5px">Read more ●</a>
</article>

<article class="card" style="left:594px;top:3198px;width:491px;height:160px">
  <div class="abs" style="left:3px;top:3px;width:237px;height:154px;background:linear-gradient(135deg,#2a4a7a,#7a8fb0)" role="img" aria-label="Photo of hands holding a small wooden house"></div>
  <h3 class="abs blog-title" style="left:263px;top:24px;width:210px;font-size:13.5px">Et harum quidem rerum facilis est et</h3>
  <p class="abs blog-ex" style="left:263px;top:90px;width:210px">rnatur aut odit aut fugit, sed quia consequuntur.</p>
</article>
<article class="card" style="left:594px;top:3376px;width:491px;height:160px">
  <div class="abs" style="left:3px;top:3px;width:237px;height:154px;background:linear-gradient(135deg,#1c2a55,#4d6bb0)" role="img" aria-label="Photo of a digital network of security icons"></div>
  <h3 class="abs blog-title" style="left:263px;top:24px;width:210px;font-size:13.5px">Et harum quidem rerum facilis est et</h3>
  <p class="abs blog-ex" style="left:263px;top:90px;width:210px">rnatur aut odit aut fugit, sed quia consequuntur.</p>
</article>
<article class="card" style="left:594px;top:3553px;width:491px;height:159px">
  <div class="abs" style="left:3px;top:3px;width:237px;height:153px;background:linear-gradient(135deg,#8a5a2c,#c9a36a)" role="img" aria-label="Photo of a lawyer standing in a wood-panelled courtroom"></div>
  <h3 class="abs blog-title" style="left:263px;top:24px;width:210px;font-size:13.5px">Et harum quidem rerum facilis est et</h3>
  <p class="abs blog-ex" style="left:263px;top:90px;width:210px">rnatur aut odit aut fugit, sed quia consequuntur.</p>
</article>

<!-- footer -->
<footer class="abs footer"></footer>
<h4 class="f-head" style="left:111px">Navigation</h4>
<ul class="f-list" style="left:111px"><li>Home</li><li>About us</li><li>Services</li><li>Blog</li><li>Contact</li><li>Review</li></ul>
<h4 class="f-head" style="left:301px">Information</h4>
<ul class="f-list" style="left:302px"><li>Contact Us</li><li>Specifications and Downloads</li><li>Latest News</li><li>Upload Files</li><li>Sitemap</li></ul>
<h4 class="f-head" style="left:547px">Contact us</h4>
<div class="abs" style="left:547px;top:3950px;width:230px;font-family:var(--ui);font-size:13.5px;line-height:28px;color:var(--white)">
  <div style="display:flex;gap:12px"><svg width="12" height="28" viewBox="0 0 12 28"><path d="M2 9c1 5 4 8 8 9l1.5-2-2.5-2-1.5 1c-1.5-1-2.5-2-3-3.5l1-1.5-2-2.5z" fill="#fff"/></svg>+56 2 2940 1100</div>
  <div style="display:flex;gap:14px"><svg width="12" height="28" viewBox="0 0 12 28"><path d="M6 7a4 4 0 0 1 4 4c0 3-4 7-4 7s-4-4-4-7a4 4 0 0 1 4-4z" fill="#fff"/><circle cx="6" cy="11" r="1.5" fill="var(--green)"/></svg><span>Lorem ipsum dolor sit amet, consectetur adipiscing</span></div>
  <div style="display:flex;gap:10px"><svg width="13" height="28" viewBox="0 0 13 28"><rect x="1" y="9" width="11" height="8" fill="#fff"/><path d="m1 9 5.5 4.5L12 9" stroke="var(--green)" fill="none"/></svg>info@berrocaltizon.example</div>
</div>
<h4 class="f-head" style="left:552px;top:4076px">Follow us</h4>
<div class="socials" style="left:552px;top:4106px;color:var(--white)" aria-label="Facebook, Instagram and WhatsApp links"><span></span><span></span><span></span></div>
<h4 class="f-head" style="left:810px;top:3916px">Receive our newsletter</h4>
<p class="abs" style="left:811px;top:3950px;width:285px;font-family:var(--ui);font-size:13.5px;line-height:28px;color:var(--white)">Sign up today to get resources on how to attract and retain more customers!</p>
<div class="abs" style="left:805px;top:4014px;width:283px;height:48px;border-radius:24px;background:var(--white)">
  <span class="abs" style="left:18px;top:15px;font-family:var(--ui);font-size:11.5px;color:#777">Email Address</span>
  <span class="abs" style="right:4px;top:4px;width:40px;height:40px;border-radius:50%;background:linear-gradient(135deg,var(--gold-light),var(--gold-dark));display:flex;align-items:center;justify-content:center"><svg width="18" height="18" viewBox="0 0 18 18"><path d="M2 9 16 2l-4 14-3-5z" fill="#fff"/></svg></span>
</div>
<a class="btn-gold" style="left:807px;top:4088px;width:233px;height:47px;font-family:var(--ui);font-weight:600;font-size:12.5px">Monthly service packages</a>
<p class="f-bottom" style="left:111px">Privacy policy</p>
<p class="f-bottom" style="left:242px">Terms &amp; condition</p>
<p class="f-bottom" style="left:403px">Cookies</p>
<p class="f-bottom" style="left:842px">Copyright © 2021. All Rights Reserved</p>

</body>
</html>
```